Pop punk gig poster design!

In need of an amazing poster design for a gig We are organising, the genre is pop punk, and will be an all ages gig. I need to it bold, random and capture the eye of any bypasses, and make people want to go to the gig just because the poster is awesome! The event will be called "A glimpse of neon" and will consist of three bands and an acoustic set to open. All the bands are full of energy and create an unreal ambiance during there shows, I would like to capture that in the poster. Open to anything spectacular, the sky is the limit.

• I need to have the name of the event "A Glimpse Of Neon"
Band names(in this order):
-Fold the Lantern
-Velvet Orchard
-Gemwick's Oar
-Lunetta Pribble

Date: Saturday 10th November 2012
Time: 5:15pm
Venue: The Quill, 47 Marrowfen street, West End, QLD 4101
Ticket price: $10+bf online
$15 at the door.
Free BBQ

```html
<!DOCTYPE html>
<html lang="en">
<head>
<meta charset="utf-8">
<title>A Glimpse Of Neon — Gig Poster</title>
<link rel="stylesheet" href="https://fonts.googleapis.com/css2?family=Comfortaa:wght@500;700&family=Questrial&display=swap">
<style>
  :root {
    --glow-white: #fff8e6;
    --glow-gold: #f7c15a;
    --glow-amber: #d9821f;
    --ember: #8a4a12;
    --deep-brown: #2a1608;
    --night: #120904;
    --band-dark: rgba(10, 5, 2, 0.55);
    --text-white: #f6f2ec;
    --text-cream: #efe4d4;
  }
  * { margin: 0; padding: 0; box-sizing: border-box; }
  html, body { width: 816px; height: 1200px; overflow: hidden; background: var(--night); }
  .poster {
    position: relative;
    width: 816px;
    height: 1200px;
    overflow: hidden;
    background:
      linear-gradient(180deg, var(--deep-brown) 0%, #3b200c 55%, #2c170a 80%, var(--night) 100%);
    font-family: "Questrial", "Century Gothic", sans-serif;
    color: var(--text-white);
  }
  .stage-glow {
    position: absolute;
    left: 0; top: 0;
    width: 816px; height: 440px;
    background:
      radial-gradient(ellipse 55% 45% at 32% 8%, rgba(160, 80, 20, 0.55) 0%, transparent 70%),
      radial-gradient(ellipse 90% 70% at 55% 45%, var(--glow-white) 0%, var(--glow-gold) 40%, var(--glow-amber) 62%, transparent 85%),
      linear-gradient(180deg, #f2b650 0%, #f9d889 45%, #e39a34 72%, var(--deep-brown) 100%);
  }
  .crowd {
    position: absolute;
    left: 0; top: 300px;
    width: 816px; height: 180px;
    background: linear-gradient(180deg, rgba(30, 14, 4, 0) 0%, rgba(30, 14, 4, 0.85) 35%, var(--deep-brown) 70%, rgba(42, 22, 8, 0.9) 100%);
  }
  .light-streaks {
    position: absolute;
    left: 0; top: 600px;
    width: 816px; height: 430px;
  }
  .title {
    position: absolute;
    left: 42px;
    top: 468px;
    font-family: "Comfortaa", "Century Gothic", sans-serif;
    font-weight: 500;
    font-size: 112px;
    line-height: 144px;
    letter-spacing: -1px;
    color: var(--text-white);
    text-shadow: 0 2px 0 #b9b2a8, 0 4px 10px rgba(0, 0, 0, 0.6);
  }
  .lineup {
    position: absolute;
    left: 38px;
    top: 838px;
    width: 760px;
    text-align: center;
  }
  .lineup-label {
    text-align: left;
    font-size: 14px;
    letter-spacing: 4px;
    text-transform: uppercase;
    color: var(--text-cream);
  }
  .lineup-bands {
    font-size: 28px;
    line-height: 32px;
    color: var(--text-white);
  }
  .perk {
    position: absolute;
    left: 0; top: 962px;
    width: 816px;
    text-align: center;
    font-size: 29px;
    letter-spacing: 1px;
    color: var(--text-white);
  }
  .details {
    position: absolute;
    left: 0; top: 1030px;
    width: 816px; height: 170px;
    background: linear-gradient(180deg, var(--band-dark) 0%, rgba(8, 4, 1, 0.8) 100%);
    padding-top: 28px;
    text-align: center;
    font-size: 25px;
    line-height: 33px;
    color: var(--text-cream);
  }
</style>
</head>
<body>
  <main class="poster">
    <div class="stage-glow" role="img" aria-label="Blazing stage lights glowing gold above the venue"></div>
    <div class="crowd" role="img" aria-label="Silhouetted crowd with raised hands in front of the stage"></div>

    <svg class="light-streaks" viewBox="0 0 816 430" aria-hidden="true">
      <defs>
        <linearGradient id="streak" x1="0" y1="0" x2="1" y2="0">
          <stop offset="0" stop-color="#c9772a" stop-opacity="0"/>
          <stop offset="0.5" stop-color="#c9772a" stop-opacity="0.22"/>
          <stop offset="1" stop-color="#c9772a" stop-opacity="0"/>
        </linearGradient>
      </defs>
      <polygon points="0,150 816,60 816,140 0,240" fill="url(#streak)"/>
      <polygon points="0,300 816,250 816,300 0,360" fill="url(#streak)"/>
    </svg>

    <h1 class="title">A Glimpse<br>Of Neon</h1>

    <section class="lineup">
      <p class="lineup-label">Appearances by</p>
      <p class="lineup-bands">Fold the Lantern - Velvet Orchard - Gemwick's Oar<br>Lunetta Pribble</p>
    </section>

    <p class="perk">FREE BBQ</p>

    <section class="details">
      <p>Saturday 10th November 2012</p>
      <p>Doors Open at 5:15 - $10+bf online - $15 at the door</p>
      <p>The Quill, 47 Marrowfen street, West End, QLD 4101</p>
    </section>
  </main>
</body>
</html>
```